Create a professional, eye-catching business card design that reflects the values and services of Brookfern Veterinary Hospital. we provide veterinary services and the business card should be a memorable representation of the clinic and align with its branding and mission. our tag line is "Faithful Friends, Gentle Lasting Care"
Use clean, modern typography. Prioritize readability and professionalism. We would like to see designs that use the color blue, as in the logo example. the final design should communicate professionalism and care, with attention to detail.

```html
<!DOCTYPE html>
<html lang="en">
<head>
<meta charset="utf-8">
<title>Brookfern Veterinary Hospital – Business Card</title>
<link rel="stylesheet" href="https://fonts.googleapis.com/css2?family=Montserrat:wght@700;800&family=Open+Sans:wght@400;600;700&family=Varela+Round&display=swap">
<style>
  :root {
    --navy: #1b2d5e;
    --navy-deep: #15244d;
    --gold: #e3a51c;
    --paper: #f7f7f8;
    --paper-shade: #e9eaee;
    --ink: #2b2f3a;
    --stage: #5a5b5e;
    --ghost: #dcdee6;
  }
  * { box-sizing: border-box; margin: 0; padding: 0; }
  html, body { width: 1200px; height: 900px; overflow: hidden; }
  body {
    background: var(--stage);
    position: relative;
    font-family: "Open Sans", sans-serif;
  }
  .card {
    position: absolute;
    width: 660px;
    height: 377px;
    box-shadow: 0 18px 40px rgba(0,0,0,.35);
    overflow: hidden;
  }

  /* Front */
  .card-front {
    left: 70px; top: 55px;
    background: linear-gradient(135deg, var(--navy-deep), var(--navy));
    color: #fff;
  }
  .front-brand {
    position: absolute;
    left: 0; right: 0; top: 92px;
    text-align: center;
  }
  .brand-mark {
    display: inline-block;
    width: 54px; height: 54px;
    border: 2px solid #fff;
    border-radius: 50%;
    margin-bottom: 12px;
  }
  .brand-name {
    font-family: "Montserrat", sans-serif;
    font-weight: 800;
    font-size: 46px;
    letter-spacing: 1px;
    line-height: 1;
  }
  .brand-sub {
    font-family: "Montserrat", sans-serif;
    font-weight: 800;
    font-size: 14px;
    letter-spacing: 1.5px;
    margin-top: 6px;
  }
  .front-rule {
    position: absolute;
    left: 70px; right: 70px; top: 262px;
    height: 1.5px;
    background: var(--gold);
  }
  .tagline {
    position: absolute;
    left: 0; right: 0; top: 276px;
    text-align: center;
    font-family: "Varela Round", sans-serif;
    font-size: 19px;
    letter-spacing: 3px;
  }

  /* Back */
  .card-back {
    left: 470px; top: 470px;
    background: linear-gradient(120deg, var(--paper) 55%, var(--paper-shade));
    color: var(--ink);
  }
  .back-brand {
    position: absolute;
    left: 36px; top: 36px;
    color: var(--navy);
  }
  .back-brand .brand-mark { border-color: var(--navy); width: 40px; height: 40px; margin-bottom: 8px; }
  .back-brand .brand-name { font-size: 32px; }
  .back-brand .brand-sub { font-size: 10px; margin-top: 4px; }
  .ghost-circle {
    position: absolute;
    right: -40px; top: 10px;
    width: 300px; height: 300px;
    border-radius: 50%;
    border: 2px solid var(--ghost);
  }
  .ownership {
    position: absolute;
    left: 62px; top: 166px;
  }
  .ownership-title {
    font-weight: 700;
    font-size: 17px;
    color: var(--navy);
    letter-spacing: .3px;
  }
  .ownership-sub {
    font-size: 17px;
    color: var(--gold);
  }
  .back-rule {
    position: absolute;
    left: 300px; right: 24px; top: 204px;
    height: 1.5px;
    background: var(--gold);
  }
  .contact-list {
    position: absolute;
    left: 62px; top: 240px;
    list-style: none;
  }
  .contact-item {
    display: flex;
    align-items: center;
    gap: 10px;
    font-size: 15px;
    line-height: 27px;
  }
  .contact-item svg { width: 15px; height: 15px; fill: var(--navy); flex: none; }
</style>
</head>
<body>

<section class="card card-front" aria-label="Business card front">
  <div class="front-brand">
    <span class="brand-mark" aria-hidden="true"></span>
    <div class="brand-name">BROOKFERN</div>
    <div class="brand-sub">VETERINARY HOSPITAL</div>
  </div>
  <div class="front-rule"></div>
  <p class="tagline">Faithful Friends, Gentle Lasting Care</p>
</section>

<section class="card card-back" aria-label="Business card back">
  <div class="ghost-circle" aria-hidden="true"></div>
  <div class="back-brand">
    <span class="brand-mark" aria-hidden="true"></span>
    <div class="brand-name">BROOKFERN</div>
    <div class="brand-sub">VETERINARY HOSPITAL</div>
  </div>
  <div class="ownership">
    <div class="ownership-title">BROOKFERN FAMILY</div>
    <div class="ownership-sub">Owned Veterinary Hospital</div>
  </div>
  <div class="back-rule"></div>
  <ul class="contact-list">
    <li class="contact-item">
      <svg viewBox="0 0 24 24"><path d="M6.6 10.8a15.1 15.1 0 0 0 6.6 6.6l2.2-2.2c.3-.3.7-.4 1-.2 1.1.4 2.3.6 3.6.6.6 0 1 .4 1 1V20c0 .6-.4 1-1 1C10.6 21 3 13.4 3 4c0-.6.4-1 1-1h3.5c.6 0 1 .4 1 1 0 1.3.2 2.5.6 3.6.1.3 0 .7-.2 1z"/></svg>
      (08) 9000 4821
    </li>
    <li class="contact-item">
      <svg viewBox="0 0 24 24"><path d="M2 5h20v14H2zm2 2v.5l8 5 8-5V7zm0 3v7h16v-7l-8 5z"/></svg>
      reception@brookfernvet.com.au
    </li>
    <li class="contact-item">
      <svg viewBox="0 0 24 24"><path d="M12 2a10 10 0 1 0 0 20 10 10 0 0 0 0-20zm6.9 6h-3a15 15 0 0 0-1.3-4A8 8 0 0 1 18.9 8zM12 4c.8 1.2 1.5 2.5 1.9 4h-3.8c.4-1.5 1.1-2.8 1.9-4zM4.3 14a8 8 0 0 1 0-4h3.4a16 16 0 0 0 0 4zm.8 2h3a15 15 0 0 0 1.3 4A8 8 0 0 1 5.1 16zm3-8h-3a8 8 0 0 1 4.3-4 15 15 0 0 0-1.3 4zM12 20c-.8-1.2-1.5-2.5-1.9-4h3.8c-.4 1.5-1.1 2.8-1.9 4zm2.3-6H9.7a14 14 0 0 1 0-4h4.6a14 14 0 0 1 0 4zm.3 6a15 15 0 0 0 1.3-4h3a8 8 0 0 1-4.3 4zm1.7-6a16 16 0 0 0 0-4h3.4a8 8 0 0 1 0 4z"/></svg>
      www.brookfernvet.com.au
    </li>
    <li class="contact-item">
      <svg viewBox="0 0 24 24"><path d="M12 2a7 7 0 0 0-7 7c0 5.3 7 13 7 13s7-7.7 7-13a7 7 0 0 0-7-7zm0 9.5A2.5 2.5 0 1 1 12 6.5a2.5 2.5 0 0 1 0 5z"/></svg>
      12 Ferncrest Road, Brookvale, WA 6999
    </li>
  </ul>
</section>

</body>
</html>
```